Website needed for Entertainment Company [Wordpress & Mobile Site] (Contest)

"Tumble Scholars" does Acrobatic Educational Shows for schools.
We need a 4-Page Wordpress site, for BOTH Desktop & Mobile
THINGS WE'D LIKE ON THE HOME PAGE
- Book Now buttons
- Panel advertising "Kindness-Shield Tumbling Tour" with subheading "Educating the Victim, Empowering the Bystander, and Enlightening the Bully" with Photo & 'Read More'
- text somewhere saying "Tumble Scholars engages children in important topics, by utilising Parkour & Acrobatics to captivate and enthrall todays youngest generation."
- Panel advertising Teachers Resources: "Curriculum based resources for teachers including lesson plans, workbooks, and physical activities for before & after the show." Maybe even some boxes that say a subject that is covered (eg. Mathematics. Science. PD/H/PE.)
- Everything else that you recommend
4 PAGES:
- Home Page
- About Us
- Our Program & Shows
- Teachers Resources Portal
NOTE: Transparent & Source files for logo will be provided soon (recently finished being designed)

```html
<!DOCTYPE html>
<html lang="en">
<head>
<meta charset="utf-8">
<title>Tumble Scholars — Home</title>
<link href="https://fonts.googleapis.com/css2?family=Lato:ital,wght@0,400;0,700;0,900;1,400&family=Raleway:wght@400;600;700&display=swap" rel="stylesheet">
<style>
:root{
  --orange:#f28a1e;
  --orange-dark:#e0661a;
  --green:#5aa431;
  --blue:#1c7fc4;
  --blue-bright:#1a9be0;
  --navy:#1c2430;
  --ink:#333a42;
  --muted:#7a8088;
  --line:#e3e5e8;
  --paper:#ffffff;
  --soft:#f5f6f7;
}
*{box-sizing:border-box;margin:0;padding:0}
html,body{width:1200px;height:3436px;overflow:hidden}
body{font-family:"Lato",Arial,sans-serif;color:var(--ink);background:var(--paper);position:relative}
h1,h2,h3,h4{font-family:"Raleway","Lato",sans-serif}

/* header */
.site-header{height:112px;background:var(--paper);position:relative;border-bottom:1px solid var(--line)}
.brand{position:absolute;left:40px;top:22px;display:flex;align-items:center;gap:12px}
.brand-dot{width:34px;height:34px;border-radius:50%;background:var(--orange)}
.brand-name{font-family:"Lato",sans-serif;font-weight:900;font-size:30px;color:var(--blue)}
.contact-strip{position:absolute;right:0;top:0;height:34px;display:flex;align-items:center;gap:34px;font-size:13px;color:var(--muted)}
.contact-strip span{display:flex;align-items:center;gap:7px}
.book-now{background:var(--navy);color:#fff;font-weight:700;font-size:15px;letter-spacing:1px;height:34px;padding:0 36px;display:flex;align-items:center}
.main-nav{position:absolute;right:40px;top:66px;display:flex;gap:30px;font-size:14px;text-transform:uppercase;color:var(--ink)}
.main-nav a{color:inherit;text-decoration:none}
.main-nav .current{color:var(--orange)}

/* hero */
.hero{position:relative;height:568px;background:linear-gradient(100deg,#3c3a38 0%,#6b5a4c 40%,#8a7462 70%,#5d5048 100%)}
.hero-photo{position:absolute;inset:0;background:linear-gradient(90deg,rgba(20,20,22,.55),rgba(20,20,22,.1) 70%)}
.hero-copy{position:absolute;left:76px;top:228px;color:#fff;width:520px}
.hero-copy h1{font-size:40px;font-weight:700;line-height:1.15;margin-bottom:20px}
.hero-copy p{font-size:19px;line-height:1.4;margin-bottom:26px}
.search{display:flex;width:440px;height:44px}
.search .field{flex:1;background:rgba(255,255,255,.22);color:#fff;font-size:14px;padding:0 16px;display:flex;align-items:center}
.search .go{background:var(--orange);color:#fff;font-weight:700;font-size:14px;padding:0 24px;display:flex;align-items:center}
.feature-stack{position:absolute;left:816px;top:216px;width:290px;z-index:2}
.feature{height:124px;color:#fff;display:flex;gap:18px;padding:22px;margin-bottom:10px;box-shadow:0 6px 14px rgba(0,0,0,.25)}
.feature.orange{background:var(--orange-dark)}
.feature.green{background:var(--green)}
.feature.blue{background:var(--blue)}
.feature svg{flex:none}
.feature h3{font-size:19px;margin-bottom:6px}
.feature p{font-size:13px;line-height:1.4}

/* welcome */
.welcome{position:relative;height:700px}
.topic-grid{position:absolute;left:90px;top:110px;width:480px;height:500px}
.topic{position:absolute;width:124px;height:124px;background:var(--paper);border:1px solid var(--line);box-shadow:0 2px 8px rgba(0,0,0,.08);display:flex;flex-direction:column;align-items:center;justify-content:center;gap:12px;font-size:16px}
.welcome-copy{position:absolute;left:658px;top:130px;width:460px}
.welcome-copy h2{font-size:38px;font-weight:600;line-height:1.15;margin-bottom:18px;color:var(--navy)}
.welcome-copy p{font-size:13px;line-height:1.6;color:var(--muted);margin-bottom:16px}
.btn-blue{display:inline-block;background:var(--blue);color:#fff;font-weight:700;font-size:14px;letter-spacing:1px;padding:16px 42px;margin-top:14px;box-shadow:0 6px 14px rgba(28,127,196,.35)}

/* resources */
.resources{position:relative;height:920px;background:linear-gradient(180deg,#2b2d31,#4a3f38 50%,#2c2b2c)}
.resources-photo{position:absolute;inset:0;background:rgba(15,17,20,.55)}
.resources-head{position:relative;text-align:center;color:#fff;padding-top:92px}
.resources-head h2{font-size:44px;font-weight:600;margin-bottom:14px}
.resources-head p{font-size:22px;font-style:italic;line-height:1.4;width:760px;margin:0 auto}
.subjects{position:absolute;left:80px;top:292px;width:1040px;display:grid;grid-template-columns:repeat(3,330px);gap:40px 25px}
.subject{height:220px;padding:28px 26px;color:#fff}
.subject h3{font-size:20px;margin:10px 0 10px}
.subject p{font-size:13px;line-height:1.5;opacity:.9}
.s-math{background:rgba(150,55,35,.6)}
.s-sci{background:rgba(95,110,80,.55)}
.s-pe{background:rgba(110,60,120,.55)}
.s-eng{background:rgba(40,90,120,.55)}
.s-art{background:rgba(150,95,40,.55)}
.s-soc{background:rgba(35,60,110,.55)}

/* testimonial */
.testimonial{height:500px;text-align:center;padding-top:66px}
.quote-mark{font-family:"Raleway",sans-serif;font-size:70px;color:var(--blue-bright);line-height:1}
.testimonial h4{font-size:24px;font-weight:600;margin:10px 0 8px;color:var(--navy)}
.stars{display:flex;gap:4px;justify-content:center;margin-bottom:22px}
.testimonial blockquote{width:760px;margin:0 auto 32px;font-size:17px;font-style:italic;line-height:1.6;color:var(--muted)}
.avatars{display:flex;gap:22px;justify-content:center}
.avatar{width:84px;height:84px;border-radius:50%;background:linear-gradient(135deg,#c9a88c,#8c6a55)}
.avatar.on{outline:3px solid var(--blue-bright);outline-offset:3px}

/* cta */
.cta{position:relative;height:400px;background:linear-gradient(100deg,#0d6eb6,#1a9be0 60%,#2aa8e8)}
.cta-copy{position:absolute;left:76px;top:112px;width:560px;color:#fff}
.cta-copy p{font-size:24px;font-style:italic;line-height:1.45;margin-bottom:30px}
.btn-orange{display:inline-block;background:var(--orange);color:#fff;font-weight:700;font-size:14px;letter-spacing:1px;padding:16px 42px}
.contact-card{position:absolute;left:780px;top:82px;width:340px;height:256px;background:#fff;padding:26px 30px;box-shadow:0 8px 22px rgba(0,0,0,.2)}
.contact-card h3{font-size:22px;font-weight:600;margin-bottom:20px;color:var(--navy)}
.contact-card .input{height:38px;border-bottom:1px solid var(--line);font-size:13px;color:#a8adb3;display:flex;align-items:center;margin-bottom:10px}
.contact-card .subscribe{margin-top:22px;background:var(--blue);color:#fff;font-weight:700;font-size:14px;letter-spacing:1px;height:46px;display:flex;align-items:center;justify-content:center}

/* footer */
.site-footer{height:236px;background:var(--paper);text-align:center;padding-top:48px}
.social{display:flex;gap:14px;justify-content:center;margin-bottom:38px}
.social span{width:46px;height:46px;border-radius:6px}
.footer-nav{display:flex;justify-content:center;gap:22px;font-size:14px;color:var(--muted);margin-bottom:16px}
.copyright{font-size:12px;color:#a0a5ab}
</style>
</head>
<body>

<header class="site-header">
  <div class="brand"><span class="brand-dot"></span><span class="brand-name">Tumble Scholars</span></div>
  <div class="contact-strip">
    <span><svg width="14" height="14" viewBox="0 0 24 24"><path d="M6 2h4l2 5-3 2a11 11 0 0 0 6 6l2-3 5 2v4a2 2 0 0 1-2 2A18 18 0 0 1 4 4a2 2 0 0 1 2-2z" fill="#7a8088"/></svg>555 010 2468</span>
    <span><svg width="15" height="12" viewBox="0 0 24 18"><rect x="1" y="1" width="22" height="16" fill="none" stroke="#7a8088" stroke-width="2"/><path d="M1 1l11 9 11-9" fill="none" stroke="#7a8088" stroke-width="2"/></svg>hello@tumblescholars.example</span>
    <span class="book-now">BOOK NOW</span>
  </div>
  <nav class="main-nav">
    <a class="current">Home</a><a>About Us</a><a>Our Program &amp; Shows</a><a>Teacher Resources</a><a>Contact</a>
  </nav>
</header>

<section class="hero">
  <div class="hero-photo" role="img" aria-label="Photo of smiling school students in a classroom"></div>
  <div class="hero-copy">
    <h1>Kindness-Shield Tumbling Tour</h1>
    <p>Educating the Victim, Empowering the Bystander, and Enlightening the Bully</p>
    <div class="search"><span class="field">Search Course</span><span class="go">SEARCH</span></div>
  </div>
  <div class="feature-stack">
    <div class="feature orange">
      <svg width="40" height="40" viewBox="0 0 40 40"><rect x="6" y="8" width="28" height="22" fill="none" stroke="#fff" stroke-width="2.5"/><path d="M14 34h12" stroke="#fff" stroke-width="2.5"/></svg>
      <div><h3>New Classes</h3><p>Lorem Ipsum is simply dummy text of the printing and typesetting.</p></div>
    </div>
    <div class="feature green">
      <svg width="40" height="40" viewBox="0 0 40 40"><path d="M8 8h24v24H8z" fill="none" stroke="#fff" stroke-width="2.5"/><path d="M13 20l5 5 9-10" fill="none" stroke="#fff" stroke-width="2.5"/></svg>
      <div><h3>Top Shows</h3><p>Lorem Ipsum is simply dummy text of the printing and typesetting.</p></div>
    </div>
    <div class="feature blue">
      <svg width="40" height="40" viewBox="0 0 40 40"><circle cx="20" cy="20" r="13" fill="none" stroke="#fff" stroke-width="2.5"/><path d="M20 12v8l6 4" fill="none" stroke="#fff" stroke-width="2.5"/></svg>
      <div><h3>Covered Subject</h3><p>Lorem Ipsum is simply dummy text of the printing and typesetting.</p></div>
    </div>
  </div>
</section>

<section class="welcome">
  <div class="topic-grid">
    <div class="topic" style="left:170px;top:0"><svg width="36" height="36" viewBox="0 0 36 36"><path d="M4 14l14-7 14 7-14 7z M10 17v8c4 3 12 3 16 0v-8" fill="none" stroke="#555" stroke-width="2"/></svg>Education</div>
    <div class="topic" style="left:0;top:70px"><svg width="36" height="36" viewBox="0 0 36 36"><rect x="8" y="5" width="20" height="26" fill="none" stroke="#555" stroke-width="2"/><path d="M12 12h12M12 18h12M12 24h8" stroke="#555" stroke-width="2"/></svg>Curriculum</div>
    <div class="topic" style="left:340px;top:70px"><svg width="36" height="36" viewBox="0 0 36 36"><path d="M4 8h12v22H4zM20 8h12v22H20z" fill="none" stroke="#555" stroke-width="2"/></svg>Workbooks</div>
    <div class="topic" style="left:170px;top:184px"><svg width="36" height="36" viewBox="0 0 36 36"><circle cx="11" cy="22" r="6" fill="none" stroke="#555" stroke-width="2"/><circle cx="25" cy="22" r="6" fill="none" stroke="#555" stroke-width="2"/><path d="M11 16V6M25 16V6" stroke="#555" stroke-width="2"/></svg>Acrobatics</div>
    <div class="topic" style="left:0;top:254px"><svg width="36" height="36" viewBox="0 0 36 36"><path d="M4 30h10v-8h8v-8h10" fill="none" stroke="#555" stroke-width="2"/></svg>Parkour</div>
    <div class="topic" style="left:340px;top:254px"><svg width="36" height="36" viewBox="0 0 36 36"><circle cx="18" cy="18" r="12" fill="none" stroke="#555" stroke-width="2"/><path d="M6 18h24M18 6v24" stroke="#555" stroke-width="2"/></svg>Activities</div>
    <div class="topic" style="left:170px;top:368px"><svg width="36" height="36" viewBox="0 0 36 36"><path d="M6 10l12-5 12 5-12 5zM6 17l12 5 12-5M6 24l12 5 12-5" fill="none" stroke="#555" stroke-width="2"/></svg>Lesson plans</div>
  </div>
  <div class="welcome-copy">
    <h2>Welcome to Tumble Scholars</h2>
    <p>Lorem Ipsum is simply dummy text of the printing and typesetting industry. Lorem Ipsum has been the industry's standard dummy text ever since the 1500s, when an unknown printer took a galley of type and scrambled it to make a type specimen book.</p>
    <p>It has survived not only five centuries, but also the leap into electronic typesetting, remaining essentially unchanged. It was popularised in the 1960s with the release of Letraset sheets containing Lorem Ipsum passages, and more recently with desktop.</p>
    <span class="btn-blue">READ MORE</span>
  </div>
</section>

<section class="resources">
  <div class="resources-photo" role="img" aria-label="Photo of students reading books at desks"></div>
  <div class="resources-head">
    <h2>Teacher Resources</h2>
    <p>Curriculum based resources for teachers including lesson plans, workbooks, and physical activities for before &amp; after the show.</p>
  </div>
  <div class="subjects">
    <div class="subject s-math"><svg width="30" height="30" viewBox="0 0 30 30"><path d="M6 9h18M15 3v12M6 23h18M11 19l8 8M19 19l-8 8" stroke="#fff" stroke-width="2" fill="none"/></svg><h3>Mathematics</h3><p>Lorem Ipsum is simply dummy text of the printing and typesetting industry. Lorem Ipsum has been the industry's standard dummy text ever since the 1500s, when an unknown printer took a galley of type.</p></div>
    <div class="subject s-sci"><svg width="30" height="30" viewBox="0 0 30 30"><path d="M11 3h8M13 3v9L5 26h20L17 12V3" stroke="#fff" stroke-width="2" fill="none"/></svg><h3>Science</h3><p>Lorem Ipsum is simply dummy text of the printing and typesetting industry. Lorem Ipsum has been the industry's standard.</p></div>
    <div class="subject s-pe"><svg width="30" height="30" viewBox="0 0 30 30"><circle cx="15" cy="6" r="3" fill="#fff"/><path d="M15 10v9M8 14h14M15 19l-5 8M15 19l5 8" stroke="#fff" stroke-width="2" fill="none"/></svg><h3>PD/H/PE</h3><p>Lorem Ipsum is simply dummy text of the printing and typesetting industry. Lorem Ipsum has been the industry's standard dummy text ever since the 1500s, when an unknown printer took a galley of type.</p></div>
    <div class="subject s-eng"><svg width="30" height="30" viewBox="0 0 30 30"><path d="M4 6h10v20H4zM16 6h10v20H16z" stroke="#fff" stroke-width="2" fill="none"/></svg><h3>English</h3><p>Lorem Ipsum is simply dummy text of the printing and typesetting industry. Lorem Ipsum has been the industry's standard.</p></div>
    <div class="subject s-art"><svg width="30" height="30" viewBox="0 0 30 30"><circle cx="15" cy="15" r="11" stroke="#fff" stroke-width="2" fill="none"/><circle cx="11" cy="11" r="2" fill="#fff"/><circle cx="19" cy="11" r="2" fill="#fff"/><circle cx="11" cy="19" r="2" fill="#fff"/></svg><h3>Fine Arts</h3><p>Lorem Ipsum is simply dummy text of the printing and typesetting industry. Lorem Ipsum has been the industry's standard.</p></div>
    <div class="subject s-soc"><svg width="30" height="30" viewBox="0 0 30 30"><circle cx="15" cy="15" r="11" stroke="#fff" stroke-width="2" fill="none"/><path d="M4 15h22M15 4c-5 6-5 16 0 22M15 4c5 6 5 16 0 22" stroke="#fff" stroke-width="2" fill="none"/></svg><h3>Social Studies</h3><p>Lorem Ipsum is simply dummy text of the printing and typesetting industry content here.</p></div>
  </div>
</section>

<section class="testimonial">
  <div class="quote-mark">66</div>
  <h4>Name Surname</h4>
  <div class="stars">
    <svg width="90" height="16" viewBox="0 0 90 16"><g fill="var(--orange)"><path id="st" d="M8 0l2.4 5 5.6.6-4.2 3.8 1.2 5.6L8 12.2 3 15l1.2-5.6L0 5.6 5.6 5z"/><use href="#st" x="18"/><use href="#st" x="36"/><use href="#st" x="54"/><use href="#st" x="72"/></g></svg>
  </div>
  <blockquote>Lorem Ipsum is simply dummy text of the printing and typesetting industry. Lorem Ipsum has been the industry's standard dummy text ever since the 1500s, when an unknown printer took a galley of type and scrambled it to make a type specimen book.</blockquote>
  <div class="avatars">
    <div class="avatar" role="img" aria-label="Portrait of a parent reviewer"></div>
    <div class="avatar on" role="img" aria-label="Portrait of a teacher reviewer"></div>
    <div class="avatar" role="img" aria-label="Portrait of a principal reviewer"></div>
  </div>
</section>

<section class="cta">
  <div class="cta-copy">
    <p>Tumble Scholars engages children in important topics, by utilising Parkour &amp; Acrobatics to captivate and enthrall todays youngest generation.</p>
    <span class="btn-orange">READ MORE</span>
  </div>
  <div class="contact-card">
    <h3>Get In Touch</h3>
    <div class="input">Your Name</div>
    <div class="input">Your Email</div>
    <div class="subscribe">SUBSCRIBE</div>
  </div>
</section>

<footer class="site-footer">
  <div class="social">
    <span style="background:#1da1f2"></span><span style="background:#e62117"></span><span style="background:#0a66c2"></span><span style="background:#3f729b"></span>
  </div>
  <div class="footer-nav"><span>Home</span><span>|</span><span>About us</span><span>|</span><span>Our Program &amp; Shows</span><span>|</span><span>Teacher Resources</span><span>|</span><span>Contact</span></div>
  <div class="copyright">2016 Tumble Scholars . All Rights Reserved.</div>
</footer>

</body>
</html>
```